Water Filtration Company needs a business card design using our existing logo/colours!

We design and manufacture and export specialised water filtration equipment. Our equipment will take unclean dirty water and filters to safe clean drinkable water.
We would like to see designs using our existing logo and colours (see attached "Palette") that represents clean safe drinking water (fresh, clean designs but still professional and modern). Our customers are other businesses who supply water filtration equipment, governments, and private individuals.
BUSINESS CARD DETAILS (Common details):
Tel: + 61 7 55 419 276
www: brindlepeak.com.au
Address: 3/47 Cordwell Parade
Marlow Flats NSW 2593 Australia
(please include the word Australia as we are an international company)
Must include: COMMERCIAL WATER FILTRATION EQUIPMENT
NAME NO 1:
Owen Pritch
General Manager
Mobile: +61 427 38 91 04
Email: owen@brindlepeak.com.au
NAME NO. 2:
Gina Rosk
Business Manager
Mobile: +61 409 572 148
Email: gina@brindlepeak.com.au
Must Have:
1) PRINT READY IN .AI & .PDF FORMATS
2) Also saved in file format .ai (Adobe Illustrator - compatible with CS4)
3) Use existing LOGO & COLOURS: Please use our logo (see attached file)
4) FONTS: we have used Avenir & Helvetica in the past but are open to other font types for the address etc.
Thank you!

```html
<!DOCTYPE html>
<html lang="en">
<head>
<meta charset="utf-8">
<title>Brindle Peak – Business Card</title>
<link href="https://fonts.googleapis.com/css2?family=Nunito+Sans:wght@400;600&display=swap" rel="stylesheet">
<style>
  :root {
    --backdrop: #2a2a2a;
    --teal: #009daa;
    --paper: #ffffff;
    --ink-light: #ffffff;
    --ink-soft: #d6f1f4;
  }
  * { margin: 0; padding: 0; box-sizing: border-box; }
  html, body {
    width: 1200px;
    height: 848px;
    overflow: hidden;
    background: var(--backdrop);
    font-family: "Nunito Sans", "Helvetica Neue", Arial, sans-serif;
  }
  .canvas { position: relative; width: 1200px; height: 848px; }

  .card {
    position: absolute;
    width: 570px;
    height: 328px;
  }
  .card--front {
    left: 291px; top: 68px;
    background: var(--paper);
    display: flex;
    align-items: center;
    justify-content: center;
    gap: 14px;
  }
  .brand-dot {
    width: 22px; height: 22px;
    border-radius: 50%;
    background: var(--teal);
  }
  .brand-name--front {
    color: var(--teal);
    font-size: 46px;
    font-weight: 600;
    letter-spacing: 0.5px;
  }

  .card--back {
    left: 296px; top: 433px;
    background: var(--teal);
    color: var(--ink-light);
  }
  .brand-name--back {
    position: absolute;
    left: 84px; top: 158px;
    font-size: 27px;
    font-weight: 600;
    color: var(--ink-light);
    letter-spacing: 0.3px;
  }
  .divider {
    position: absolute;
    left: 279px; top: 95px;
    width: 2px; height: 150px;
    background: var(--ink-light);
  }
  .person { position: absolute; left: 320px; top: 104px; text-align: center; width: 150px; }
  .person__name { font-size: 24px; font-weight: 400; line-height: 1.1; }
  .person__role { font-size: 14px; font-weight: 400; margin-top: 6px; }

  .contacts { position: absolute; left: 308px; top: 160px; font-size: 10.5px; line-height: 1.45; color: var(--ink-soft); }
  .contact { display: flex; align-items: flex-start; margin-bottom: 6px; }
  .contact__icon { width: 20px; height: 14px; margin-right: 8px; flex: none; }
  .contact__text { white-space: nowrap; }
</style>
</head>
<body>
<div class="canvas">

  <section class="card card--front">
    <span class="brand-dot"></span>
    <span class="brand-name brand-name--front">brindle peak</span>
  </section>

  <section class="card card--back">
    <span class="brand-name brand-name--back">brindle peak</span>
    <span class="divider"></span>

    <div class="person">
      <p class="person__name">Owen Pritch</p>
      <p class="person__role">General Manager</p>
    </div>

    <div class="contacts">
      <div class="contact">
        <svg class="contact__icon" viewBox="0 0 20 14" aria-hidden="true">
          <rect x="1" y="1" width="18" height="12" fill="var(--ink-soft)"/>
          <path d="M1 1 L10 8 L19 1" fill="none" stroke="var(--teal)" stroke-width="1.2"/>
        </svg>
        <span class="contact__text">owen@brindlepeak.com.au</span>
      </div>
      <div class="contact">
        <svg class="contact__icon" viewBox="0 0 20 14" aria-hidden="true">
          <rect x="6" y="0" width="8" height="14" rx="1.5" fill="none" stroke="var(--ink-soft)" stroke-width="1.4"/>
          <rect x="8" y="2" width="4" height="5" fill="var(--ink-soft)"/>
        </svg>
        <span class="contact__text">+61 427 38 91 04</span>
      </div>
      <div class="contact">
        <svg class="contact__icon" viewBox="0 0 20 14" aria-hidden="true">
          <path d="M10 14 C6 9 5 7 5 5 A5 5 0 0 1 15 5 C15 7 14 9 10 14 Z" fill="var(--ink-soft)"/>
          <circle cx="10" cy="5" r="1.8" fill="var(--teal)"/>
        </svg>
        <span class="contact__text">3/47 Cordwell Parade<br>Marlow Flats NSW<br>2593 Australia</span>
      </div>
    </div>
  </section>

</div>
</body>
</html>
```